Flyer Design

Mobile (Dustless) Shot Blasting.Graffiti Removal, Brick and Stone restoration, Paint Stripping from garden gates to Ships.No job too big or Small.No Chemicals - just Air, Water and recycled abrasive.Fully pressure controlled to prevent damage to underlying surfaces.

Target Market(s)

Domestic and commercial

Industry/Entity Type

Paint

Requirements
Nice to have
• Before and after paint removal to bare steel.
• Before and after cleaned brick/ stone work and graffiti removal

```html
<!DOCTYPE html>
<html lang="en">
<head>
<meta charset="utf-8">
<title>Ridgeline Blasting Flyer</title>
<link rel="stylesheet" href="https://fonts.googleapis.com/css2?family=Oswald:wght@400;500;600&family=Roboto+Condensed:wght@700&family=Lato:wght@400;700&display=swap">
<style>
  :root {
    --green: #3fa535;
    --green-dark: #2c7f26;
    --green-light: #67c25a;
    --charcoal: #2b2b2b;
    --charcoal-deep: #1d1d1d;
    --white: #ffffff;
    --silver: #cfd3d6;
    --backdrop: #3a3a3a;
    --photo-light: #b9bdc0;
    --photo-dark: #6f7479;
  }
  * { margin: 0; padding: 0; box-sizing: border-box; }
  html, body {
    width: 907px; height: 1200px; overflow: hidden;
    background: var(--backdrop);
  }
  .flyer {
    position: absolute; left: 103px; top: 105px;
    width: 700px; height: 990px;
    background: var(--white);
    overflow: hidden;
    box-shadow: 0 6px 24px rgba(0,0,0,.45);
  }
  .flyer-shapes { position: absolute; inset: 0; }
  .abs { position: absolute; white-space: nowrap; }

  .brand {
    left: 440px; top: 70px; width: 215px;
    display: flex; align-items: center; gap: 12px;
  }
  .brand-dot { width: 40px; height: 40px; border-radius: 50%; background: var(--white); flex: none; }
  .brand-name {
    font-family: 'Oswald', sans-serif; font-weight: 500; font-size: 26px;
    line-height: 1.05; color: var(--white); text-transform: uppercase; white-space: normal;
  }

  .tagline { left: 420px; width: 250px; text-align: right; font-family: 'Oswald', sans-serif; text-transform: uppercase; line-height: 1.2; }
  .tagline-top { top: 210px; font-size: 40px; font-weight: 400; color: var(--white); }
  .tagline-bottom { top: 256px; font-size: 50px; font-weight: 600; color: #111; letter-spacing: 1px; }

  .services { left: 38px; top: 500px; width: 240px; list-style: none; white-space: normal; }
  .services li {
    display: flex; gap: 10px; margin-bottom: 12px;
    font-family: 'Roboto Condensed', sans-serif; font-weight: 700; font-size: 17px;
    line-height: 22px; color: var(--green-light);
  }
  .services li::before {
    content: ""; flex: none; width: 12px; height: 12px; margin-top: 5px;
    border: 2px solid var(--white); border-radius: 50%;
  }

  .contact-name {
    left: 36px; top: 636px; font-family: 'Oswald', sans-serif; font-weight: 400;
    font-size: 44px; line-height: 1.2; color: var(--white); letter-spacing: .5px;
  }
  .contact-company {
    left: 37px; top: 706px; font-family: 'Lato', sans-serif; font-weight: 700;
    font-size: 24px; color: var(--white);
  }
  .contact-phone {
    left: 38px; top: 752px; display: flex; align-items: center; gap: 10px;
    font-family: 'Oswald', sans-serif; font-size: 38px; line-height: 1.2; color: var(--green-light);
  }

  .headline {
    left: 345px; top: 436px; font-family: 'Oswald', sans-serif; font-weight: 500;
    font-size: 54px; line-height: 1.2; color: var(--green);
  }
  .method {
    font-family: 'Roboto Condensed', sans-serif; font-weight: 700; font-size: 21px;
    color: var(--green-light); text-align: center; line-height: 42px;
  }
  .method-air { left: 392px; top: 553px; width: 190px; }
  .method-water { left: 392px; top: 662px; width: 190px; }
  .method-abrasive { left: 372px; top: 771px; width: 210px; }

  .footer {
    font-family: 'Lato', sans-serif; font-size: 17px; color: var(--white);
    display: flex; align-items: center; gap: 10px;
  }
  .footer svg { flex: none; }
</style>
</head>
<body>
<div class="flyer">
  <svg class="flyer-shapes" viewBox="0 0 700 990" width="700" height="990">
    <defs>
      <linearGradient id="greenFill" x1="0" y1="0" x2="0" y2="1">
        <stop offset="0" stop-color="var(--green-dark)"/>
        <stop offset=".6" stop-color="var(--green)"/>
        <stop offset="1" stop-color="var(--green-light)"/>
      </linearGradient>
      <linearGradient id="photoFill" x1="0" y1="0" x2="1" y2="1">
        <stop offset="0" stop-color="var(--photo-light)"/>
        <stop offset="1" stop-color="var(--photo-dark)"/>
      </linearGradient>
    </defs>
    <path d="M0 0 H700 V395 C560 355 430 370 320 420 L0 440 Z" fill="url(#greenFill)"/>
    <path d="M320 420 C430 370 560 355 700 395" fill="none" stroke="var(--silver)" stroke-width="6"/>
    <circle cx="150" cy="200" r="254" fill="var(--green)"/>
    <circle cx="150" cy="200" r="250" fill="var(--silver)"/>
    <circle cx="150" cy="200" r="244" fill="url(#photoFill)" role="img" aria-label="Photo of a worker in protective gear blasting a concrete surface"/>
    <path d="M22 460 H305 V810 L170 870 L22 810 Z" fill="var(--charcoal)"/>
    <path d="M0 880 Q350 815 700 860 V990 H0 Z" fill="var(--silver)"/>
    <path d="M0 888 Q350 830 700 872 V990 H0 Z" fill="var(--green)"/>
    <path d="M0 896 Q350 842 700 882 V990 H0 Z" fill="var(--charcoal-deep)"/>
    <g fill="var(--charcoal)">
      <rect x="392" y="553" width="230" height="42" rx="21"/>
      <rect x="392" y="662" width="230" height="42" rx="21"/>
      <rect x="366" y="771" width="256" height="42" rx="21"/>
    </g>
    <g>
      <circle cx="622" cy="572" r="42" fill="var(--charcoal)"/>
      <circle cx="622" cy="572" r="35" fill="var(--green)" stroke="var(--white)" stroke-width="3"/>
      <path d="M600 566 H626 a7 7 0 1 0 -7 -7 M600 577 H632 a7 7 0 1 1 -7 7" fill="none" stroke="var(--white)" stroke-width="3" stroke-linecap="round"/>
      <circle cx="622" cy="681" r="42" fill="var(--charcoal)"/>
      <circle cx="622" cy="681" r="35" fill="var(--green)" stroke="var(--white)" stroke-width="3"/>
      <path d="M614 668 C608 678 605 682 605 687 a9 9 0 0 0 18 0 C623 682 620 678 614 668 Z" fill="var(--white)"/>
      <path d="M632 668 C628 675 626 678 626 681 a6 6 0 0 0 12 0 C638 678 636 675 632 668 Z" fill="var(--white)"/>
      <circle cx="622" cy="790" r="42" fill="var(--charcoal)"/>
      <circle cx="622" cy="790" r="35" fill="var(--green)" stroke="var(--white)" stroke-width="3"/>
      <path d="M606 798 L622 772 L638 798 Z" fill="none" stroke="var(--white)" stroke-width="3" stroke-linejoin="round"/>
    </g>
  </svg>

  <div class="abs brand">
    <span class="brand-dot"></span>
    <span class="brand-name">Cleanstream Blasting</span>
  </div>

  <p class="abs tagline tagline-top">No job too big</p>
  <p class="abs tagline tagline-bottom">or small</p>

  <ul class="abs services">
    <li>Graffiti Removal</li>
    <li>Brick and Stone restoration</li>
    <li>Paint Stripping from garden gates to Ship</li>
  </ul>

  <p class="abs contact-name">DANIEL MARSH</p>
  <p class="abs contact-company">Ridgeline Blasting</p>
  <p class="abs contact-phone">
    <svg width="26" height="26" viewBox="0 0 24 24"><path d="M6.6 10.8a15 15 0 0 0 6.6 6.6l2.2-2.2a1 1 0 0 1 1-.25 11.4 11.4 0 0 0 3.6.57 1 1 0 0 1 1 1V20a1 1 0 0 1-1 1A17 17 0 0 1 3 4a1 1 0 0 1 1-1h3.5a1 1 0 0 1 1 1c0 1.25.2 2.45.57 3.57a1 1 0 0 1-.25 1z" fill="var(--white)"/></svg>
    0700 900 4512
  </p>

  <p class="abs headline">NO CHEMICALS</p>
  <p class="abs method method-air">Just Air</p>
  <p class="abs method method-water">Water</p>
  <p class="abs method method-abrasive">Recycled abrasive</p>

  <p class="abs footer" style="left:45px; top:902px;">
    <svg width="14" height="18" viewBox="0 0 14 18"><rect x="1" y="1" width="12" height="16" rx="2" fill="none" stroke="var(--green)" stroke-width="2"/><rect x="4" y="13" width="6" height="2" fill="var(--green)"/></svg>
    0700 900 4512
  </p>
  <p class="abs footer" style="left:45px; top:934px;">
    <svg width="16" height="16" viewBox="0 0 24 24"><path d="M6.6 10.8a15 15 0 0 0 6.6 6.6l2.2-2.2a1 1 0 0 1 1-.25 11.4 11.4 0 0 0 3.6.57 1 1 0 0 1 1 1V20a1 1 0 0 1-1 1A17 17 0 0 1 3 4a1 1 0 0 1 1-1h3.5a1 1 0 0 1 1 1c0 1.25.2 2.45.57 3.57a1 1 0 0 1-.25 1z" fill="var(--green)"/></svg>
    (01632) 960481
  </p>
  <p class="abs footer" style="left:352px; top:895px;">
    <svg width="18" height="14" viewBox="0 0 18 14"><rect x="1" y="1" width="16" height="12" fill="var(--green)"/><path d="M1 1 L9 8 L17 1" fill="none" stroke="var(--charcoal-deep)" stroke-width="1.5"/></svg>
    hello@ridgelineblasting.co.uk
  </p>
  <p class="abs footer" style="left:352px; top:927px;">
    <svg width="17" height="17" viewBox="0 0 20 20"><circle cx="10" cy="10" r="8.5" fill="none" stroke="var(--green)" stroke-width="2"/><path d="M1.5 10 H18.5 M10 1.5 C5 6 5 14 10 18.5 M10 1.5 C15 6 15 14 10 18.5" fill="none" stroke="var(--green)" stroke-width="1.6"/></svg>
    www.ridgelineblasting.co.uk.
  </p>
</div>
</body>
</html>
```